Flyers and business cards to create

Hi,

I need some A5 FLYRS AND BUSINESS CARDS to be made WITH THE PHOTO OF HEART AND BRAIN FURNISHED HERE

My project is going to touch parents, caregivers, school or any Youth organisation. I want something easy to read with title: Bright Paths Growth Circle (BRIPGCW).
Bright Paths Growth Circle is running in partnership with the Guild of Learning Mentors and Family Wellbeing Advisers of WA Inc (GLMFW) based in Fremantle, WA.

BRIPGCW is managed by an experienced, passionate and dedicated Educational Counsellor, Relationship Educator and therapeutic group work Facilitator. Its purpose is to promote personal growth & mental health by assisting young people in learning and developing tools and skills for life. Indeed through Emotional Intelligence (E.I), students will gain self awareness, internalise principles of successful relationships, develop positive communication skills and focus on solution and goals (human development & emotional health). Also known as Emotional Intelligence.

Our programs follow Positive Education and Person Centred Learning Principles. Emotions & experiences must be explored and connected to the process of learning in order to make meaning of them.

Some of the topics are:
Self-awareness/ Acceptance of self & other/ Truth & authenticity / Owning your choices / Empathy/ Communication & building relationship / Self-esteem & self-image / Forgiveness of self & others / The value of person / Dealing with emotions / Dealing with conflict & Event analysis / Nutrition & exercise / Benefits of relaxation & meditation

Any concern about your child confidence? Does your child feel excluded or need to stand up to bully? Does your child need help and guidance expressing his/her feelings? Do you want your child to learn more about Emotional Intelligence (EI)? Develop and straigthen social & emotional skills and learn tools for life?

If sounds like something your child would benefit from contact us for more informations.
Personal coaching (One on one session) and/or Group session available (minimum of 4).

Slogan to appear on projects: Reaching out...with a helping hand
Also joined 2 photos I would like to appear and photo colours to follow.

Thank you

Maude

```html
<!DOCTYPE html>
<html lang="en">
<head>
<meta charset="utf-8">
<title>BRIPGCW – Stationery and Flyers</title>
<link href="https://fonts.googleapis.com/css2?family=Days+One&family=Open+Sans:ital,wght@0,400;0,600;0,700;0,800;1,700&display=swap" rel="stylesheet">
<style>
:root{
  --red:#ea3b24;
  --red-dark:#c92d18;
  --steel:#33628c;
  --blue:#235b9e;
  --blue-deep:#1b4a85;
  --ink:#1d1d1d;
  --paper:#ffffff;
  --soft:#e9ecef;
  --label:#f4f4f4;
}
*{box-sizing:border-box;margin:0;padding:0}
html,body{width:704px;height:1200px;overflow:hidden}
body{background:linear-gradient(180deg,#858585,#6e6e6e);font-family:"Open Sans",Arial,sans-serif;position:relative;color:var(--ink)}
.piece{position:absolute;background:var(--paper);box-shadow:0 3px 10px rgba(0,0,0,.35);overflow:hidden}
.label{position:absolute;font-family:"Open Sans",Arial,sans-serif;font-size:19px;color:var(--label);letter-spacing:.5px}
.heading{font-family:"Days One",Arial,sans-serif}
.ph{position:absolute}

/* Flyer one */
.flyer-one{left:33px;top:30px;width:255px;height:361px}
.flyer-one .title-band{position:absolute;left:0;top:0;width:100%;height:23px;background:var(--red);color:#fff;font-weight:700;font-size:10.5px;text-align:center;line-height:23px;letter-spacing:.3px}
.flyer-one .art{left:0;top:23px;width:152px;height:108px;background:radial-gradient(circle at 45% 45%,#f1c04a 0,#e5573a 35%,#3d8fb8 70%,#f4f1ea 100%)}
.flyer-one .side-panel{position:absolute;left:152px;top:23px;width:103px;height:255px;background:var(--steel);color:#fff}
.flyer-one .slogan{position:absolute;left:0;top:14px;width:100%;text-align:center;font-size:9px;line-height:18px;white-space:nowrap}
.flyer-one .slogan .org{font-size:12.5px;display:block;margin-bottom:6px}
.flyer-one .topics-title{position:absolute;left:6px;top:116px;font-size:7px;font-weight:700}
.flyer-one .topics{position:absolute;left:14px;top:128px;width:86px;font-size:5px;line-height:8.4px}
.flyer-one .topics li{list-style:disc}
.flyer-one .why{position:absolute;left:0;top:131px;width:152px;height:147px;background:var(--red);color:#fff;padding:17px 5px 0 5px;font-size:5.1px;line-height:7.3px}
.flyer-one .why-tab{position:absolute;left:44px;top:123px;width:102px;height:17px;background:#fff;border-radius:0 8px 0 0;font-family:"Days One",Arial,sans-serif;font-size:9.5px;line-height:18px;padding-left:14px;color:var(--ink)}
.flyer-one .why p+p{margin-top:5px}
.flyer-one .questions{position:absolute;left:0;top:278px;width:100%;height:54px;background:#fff;padding:6px 5px;font-size:5.2px;line-height:8.2px;color:#222}
.flyer-one .questions .mark{position:absolute;right:8px;top:4px;width:62px;height:46px;border-radius:50%;background:radial-gradient(circle at 35% 55%,#e5322a 0,#e5322a 30%,#f0c6c8 55%,#fff 75%)}
.flyer-one .contact{position:absolute;left:0;top:332px;width:100%;height:29px;background:var(--red);color:#fff;text-align:center}
.flyer-one .contact small{display:block;font-size:5px;line-height:6px;padding-top:2px}
.flyer-one .contact strong{display:block;font-size:8.5px;line-height:12px}

/* Flyer two */
.flyer-two{left:372px;top:30px;width:256px;height:361px}
.flyer-two .photo{left:0;top:0;width:100%;height:138px;background:linear-gradient(180deg,#f3f5f8 0,#e8dfd8 45%,#c9a68d 75%,#eef1f4 100%)}
.flyer-two .ask{position:absolute;left:0;top:3px;width:100%;text-align:center;font-size:13px;line-height:15px;letter-spacing:1.6px;color:#222}
.flyer-two .slogan-bar{position:absolute;left:55px;top:99px;width:201px;height:16px;background:rgba(255,255,255,.72);font-size:7.7px;font-weight:700;line-height:16px;text-align:center;color:#333}
.flyer-two .intro{position:absolute;left:0;top:138px;width:100%;height:94px;background:var(--blue);color:#fff}
.flyer-two .mark{position:absolute;left:7px;top:-7px;width:56px;height:62px;border-radius:50%;background:radial-gradient(circle at 40% 55%,#e5322a 0,#e5322a 28%,#eec7c4 52%,#fff 70%);border:2px solid #fff}
.flyer-two .intro h2{position:absolute;left:83px;top:4px;width:170px;font-family:"Days One",Arial,sans-serif;font-weight:400;font-size:11.4px;line-height:15.6px;letter-spacing:.4px}
.flyer-two .intro p{position:absolute;left:9px;top:62px;width:240px;font-size:6.4px;line-height:7.8px}
.flyer-two .learn-bar{position:absolute;left:0;top:232px;width:100%;height:16px;background:var(--soft);font-size:7.6px;font-weight:700;line-height:16px;padding-left:9px;color:#222}
.flyer-two .skills{position:absolute;left:0;top:248px;width:100%;height:74px;background:var(--blue);color:#fff}
.flyer-two .skill{position:absolute;width:80px;display:flex;align-items:center;gap:5px;font-size:6.4px;line-height:7.6px;letter-spacing:.4px}
.flyer-two .skill svg{flex:none}
.flyer-two .eq{position:absolute;left:9px;top:62px;font-size:6.8px;font-weight:700;font-style:italic}
.flyer-two .contact{position:absolute;left:0;top:322px;width:100%;height:39px;background:#fff;text-align:center;color:var(--blue)}
.flyer-two .contact small{display:block;font-size:6.6px;font-weight:700;line-height:8px;padding-top:5px}
.flyer-two .contact strong{display:block;font-size:11.5px;line-height:16px;color:var(--blue-deep)}

/* Letterhead */
.letterhead{left:39px;top:439px;width:244px;height:345px}
.letterhead .frame{position:absolute;left:0;top:0}
.letterhead .mark{position:absolute;left:24px;top:4px;width:54px;height:54px;border-radius:50%;background:#e5322a;border:3px solid #fff}
.brand{font-family:"Open Sans",Arial,sans-serif;font-weight:800;color:var(--red);letter-spacing:.3px}
.tagline{font-size:4.5px;color:#444;letter-spacing:.2px;text-transform:uppercase}
.letterhead .brand{position:absolute;left:126px;top:14px;font-size:16px;line-height:18px}
.letterhead .tagline{position:absolute;left:126px;top:33px}
.foot-text{position:absolute;color:#fff;font-size:6.8px;display:flex;align-items:center;gap:4px;white-space:nowrap}
.letterhead .foot-text{font-size:6.2px;gap:3px}

/* Envelope */
.envelope{left:117px;top:860px;width:470px;height:214px;background:linear-gradient(135deg,#ffffff,#eeeeee)}
.envelope .brand{position:absolute;left:30px;top:26px;font-size:24px;line-height:26px}
.envelope .tagline{position:absolute;left:31px;top:53px;font-size:6px}
.envelope .window{position:absolute;left:248px;top:56px;width:190px;height:70px;border:1.5px solid #b9b9b9;border-radius:12px;background:#f7f7f7}
.envelope .mark{position:absolute;left:408px;top:112px;width:48px;height:48px;border-radius:50%;background:#e5322a;border:3px solid #fff;box-shadow:0 0 0 1px #ccc}
.envelope .bands{position:absolute;left:0;bottom:0}
</style>
</head>
<body>

<!-- Flyer one -->
<section class="piece flyer-one">
  <div class="title-band">BRIGHT PATHS GROWTH CIRCLE</div>
  <div class="ph art" role="img" aria-label="Colourful painted hand prints forming the crown of a tree"></div>
  <div class="side-panel">
    <div class="slogan heading"><span class="org">(BRIPGCW)</span>REACHING OUT..<br>WITH<br>A HELPING HAND</div>
    <div class="topics-title">SOME OF THE TOPICS ARE :</div>
    <ul class="topics">
      <li>Self-awareness</li>
      <li>Acceptance of self &amp; other</li>
      <li>Truth &amp; authenticity</li>
      <li>Owning your choices Empathy</li>
      <li>Communication &amp; building relationship</li>
      <li>Self-esteem &amp; self-image</li>
      <li>Forgiveness of self &amp; others</li>
      <li>The value of person</li>
      <li>Dealing with emotions</li>
      <li>Dealing with conflict &amp; Event analysis</li>
      <li>Nutrition &amp; exercise</li>
      <li>Benefits of relaxation &amp; meditation</li>
    </ul>
  </div>
  <div class="why">
    <p>BRIPGCW is managed by an experienced, passionate and dedicated Educational Counsellor, Relationship Educator and therapeutic group work Facilitator. Its purpose is to promote personal growth &amp; mental health by assisting young people in learning and developing tools and skills for life. Indeed through Emotional Intelligence (E.I), students will gain self awareness, internalise principles of successful relationships, develop positive communication skills and focus on solution and goals (human development &amp; emotional health). Also known as Emotional Intelligence.</p>
    <p>Our programs follow Positive Education and Person Centred Learning Principles. Emotions &amp; experiences must be explored and connected to the process of learning in order to make meaning of them.</p>
  </div>
  <div class="why-tab">WHY US ?</div>
  <div class="questions">
    * Any concern about your child confidence ?<br>
    * Does your child feel excluded or need to stand up to bully ?<br>
    * Does your child need help and guidance expressing his/her feelings ?<br>
    * Do you want your child to learn more about Emotional Intelligence (EI) ?<br>
    * Develop and straigthen social &amp; emotional skills and learn tools for life ?
    <div class="mark" role="img" aria-label="Cartoon heart and brain walking hand in hand"></div>
  </div>
  <div class="contact">
    <small>IF SOUNDS LIKE SOMETHING YOUR CHILD WOULD BENEFIT FROM<br>CONTACT US FOR MORE INFORMATIONS.</small>
    <strong>+120-555010348 / +120-55501923</strong>
  </div>
</section>
<div class="label" style="left:134px;top:404px">FLYER</div>

<!-- Flyer two -->
<section class="piece flyer-two">
  <div class="ph photo" role="img" aria-label="Four cheerful young children lying down with their chins in their hands"></div>
  <div class="ask heading">ANY CONCERN ABOUT<br>YOUR CHILD CONFIDENCE ?</div>
  <div class="slogan-bar">REACHING OUT...WITH A HELPING HAND</div>
  <div class="intro">
    <div class="mark" role="img" aria-label="Cartoon heart and brain walking hand in hand"></div>
    <h2>TRY AN EFFECTIVE BRIGHT PATHS GROWTH CIRCLE PROGRAM</h2>
    <p>SEL programming is based on the understanding that the best learning emerges in the context of supportive relationships that make learning challenging, engaging and meaningful</p>
  </div>
  <div class="learn-bar">WITH “SEL” CHILDEREN ARE ABLE TO LEARN HOW TO..</div>
  <div class="skills">
    <div class="skill" style="left:9px;top:6px">
      <svg width="20" height="20" viewBox="0 0 20 20"><circle cx="10" cy="10" r="9" fill="none" stroke="#fff" stroke-width="1.3"/><path d="M10 14.5 5.8 10.3a2.4 2.4 0 0 1 4.2-2.3 2.4 2.4 0 0 1 4.2 2.3Z" fill="none" stroke="#fff" stroke-width="1.1"/></svg>
      <span>Manage<br>Emotion</span></div>
    <div class="skill" style="left:106px;top:6px">
      <svg width="20" height="20" viewBox="0 0 20 20"><circle cx="10" cy="10" r="9" fill="none" stroke="#fff" stroke-width="1.3"/><circle cx="10" cy="10" r="5.5" fill="none" stroke="#fff" stroke-width="1.1"/><circle cx="10" cy="10" r="2" fill="#fff"/></svg>
      <span>Set Positive<br>Goal</span></div>
    <div class="skill" style="left:186px;top:6px">
      <svg width="20" height="20" viewBox="0 0 20 20"><circle cx="10" cy="10" r="9" fill="none" stroke="#fff" stroke-width="1.3"/><path d="M5 10l3 3 7-7" fill="none" stroke="#fff" stroke-width="1.3"/></svg>
      <span>Feel Empathy<br>for others</span></div>
    <div class="skill" style="left:9px;top:40px">
      <svg width="20" height="20" viewBox="0 0 20 20"><circle cx="10" cy="10" r="9" fill="none" stroke="#fff" stroke-width="1.3"/><circle cx="10" cy="8" r="3" fill="none" stroke="#fff" stroke-width="1.1"/><path d="M5 15c1-3 9-3 10 0" fill="none" stroke="#fff" stroke-width="1.1"/></svg>
      <span>Self<br>Aawareness</span></div>
    <div class="skill" style="left:106px;top:40px">
      <svg width="20" height="20" viewBox="0 0 20 20"><path d="M10 2l7 3v5c0 4-3 7-7 8-4-1-7-4-7-8V5Z" fill="none" stroke="#fff" stroke-width="1.3"/><path d="M6.5 10l2.5 2.5 4.5-4.5" fill="none" stroke="#fff" stroke-width="1.2"/></svg>
      <span>Truth &amp;<br>Authenticity</span></div>
    <div class="skill" style="left:186px;top:40px">
      <svg width="20" height="20" viewBox="0 0 20 20"><circle cx="10" cy="10" r="9" fill="#fff"/><circle cx="10" cy="6" r="2" fill="#235b9e"/><path d="M5 14h10l-2-5H7Z" fill="#235b9e"/></svg>
      <span>Relaxation &amp;<br>Meditation</span></div>
    <div class="eq">SOCIAL AND EMOTIONAL LEARNING BUILDS EQ AND LIFE SKILLS</div>
  </div>
  <div class="contact">
    <small>IF SOUNDS LIKE SOMETHING YOUR CHILD WOULD BENEFIT FROM<br>CONTACT US FOR MORE INFORMATIONS.</small>
    <strong>+120-555010348 / +120-55501923</strong>
  </div>
</section>
<div class="label" style="left:474px;top:410px">FLYER</div>

<!-- Letterhead -->
<section class="piece letterhead">
  <svg class="frame" width="244" height="345" viewBox="0 0 244 345">
    <rect x="0" y="0" width="244" height="42" fill="#1d1d1d"/>
    <path d="M0 42 H244 V10 H134 Q118 10 116 26 Q114 42 100 42 Z" fill="#fff"/>
    <rect x="0" y="300" width="244" height="45" fill="#1d1d1d"/>
    <path d="M0 302 H150 Q140 304 136 318 Q132 330 116 330 H0 Z" fill="#ea3b24"/>
  </svg>
  <div class="mark" aria-hidden="true"></div>
  <div class="brand">BRIPGCW</div>
  <div class="tagline">Bright Paths Growth Circle</div>
  <div class="foot-text" style="left:8px;top:311px">
    <svg width="7" height="9" viewBox="0 0 8 10"><path d="M4 10S0 5.6 0 4a4 4 0 0 1 8 0c0 1.6-4 6-4 6Z" fill="#fff"/><circle cx="4" cy="4" r="1.4" fill="#ea3b24"/></svg>
    PO Box 41870, Harbor Vale, FL 33910</div>
  <div class="foot-text" style="left:146px;top:311px">
    <svg width="8" height="8" viewBox="0 0 10 10"><circle cx="5" cy="5" r="4.4" fill="none" stroke="#fff"/><path d="M3.5 3c.3 2 1.5 3.3 3.3 3.8l.6-.8" fill="none" stroke="#fff"/></svg>
    (239) 555 - 0142</div>
  <div class="foot-text" style="left:146px;top:327px">
    <svg width="8" height="8" viewBox="0 0 10 10"><circle cx="5" cy="5" r="4.4" fill="none" stroke="#fff"/><path d="M.6 5h8.8M5 .6c2 2.4 2 6.4 0 8.8M5 .6c-2 2.4-2 6.4 0 8.8" fill="none" stroke="#fff" stroke-width=".8"/></svg>
    www.brightpathscircle.com</div>
</section>
<div class="label" style="left:98px;top:794px">LETTERHEAD</div>

<div class="label" style="left:418px;top:740px">VISITING CARD</div>

<!-- Envelope -->
<section class="piece envelope">
  <div class="brand">BRIPGCW</div>
  <div class="tagline">Bright Paths Growth Circle</div>
  <div class="window"></div>
  <svg class="bands" width="470" height="64" viewBox="0 0 470 64">
    <rect x="0" y="0" width="470" height="64" fill="#1d1d1d"/>
    <path d="M0 4 H300 Q288 6 284 20 Q280 36 262 36 H0 Z" fill="#ea3b24"/>
  </svg>
  <div class="mark" aria-hidden="true"></div>
  <div class="foot-text" style="left:16px;top:164px;font-size:10px">
    <svg width="9" height="12" viewBox="0 0 8 10"><path d="M4 10S0 5.6 0 4a4 4 0 0 1 8 0c0 1.6-4 6-4 6Z" fill="#fff"/><circle cx="4" cy="4" r="1.4" fill="#ea3b24"/></svg>
    PO Box 41870, Harbor Vale, FL 33910</div>
  <div class="foot-text" style="left:316px;top:170px;font-size:9px">
    <svg width="10" height="10" viewBox="0 0 10 10"><circle cx="5" cy="5" r="4.4" fill="none" stroke="#fff"/><path d="M3.5 3c.3 2 1.5 3.3 3.3 3.8l.6-.8" fill="none" stroke="#fff"/></svg>
    (239) 555 - 0142</div>
  <div class="foot-text" style="left:316px;top:188px;font-size:9px">
    <svg width="10" height="10" viewBox="0 0 10 10"><circle cx="5" cy="5" r="4.4" fill="none" stroke="#fff"/><path d="M.6 5h8.8M5 .6c2 2.4 2 6.4 0 8.8M5 .6c-2 2.4-2 6.4 0 8.8" fill="none" stroke="#fff" stroke-width=".8"/></svg>
    www.brightpathscircle.com</div>
</section>
<div class="label" style="left:418px;top:1090px">ENVELOPE</div>

</body>
</html>
```